Electrician Business needs flyer for discount offer and advertise services

Need a promotional flyer that will grab attention,, offer:

During the months of October & November receive a 10% discount on;
Ceiling fan installation
Smoke alarm installation
Replace existing downlights for new LED downlights.
Offer expires 30th November 2016
'Keep cool, stay safe and save power with VoltMate'

Would like to advertise services and quality on reverse-side. Can have graphic pointing to reverse side on both sides, encouraging customer to read both sides of flyer.
Contact details both sides
Design to suit two-sided A5

Reverse side list services;

All residential & commercial electrical services
Electrical contracting
Real estate/strata electrical maintenance & repairs
New builds
Renovations
Security sensor lighting
Ceiling fans
Smoke Alarms
Data connections

Target Market(s)

Residential home owners and commercial, building and construction companies

Industry/Entity Type

Electrical

Font styles to use
Serif

Colors
0255a3
ffffff

Requirements
Nice to have
• A picture of a modern ceiling fan.
• Arrow/graphic pointing to reverse side, so customer reads both sides of flyer

```html
<!DOCTYPE html>
<html lang="en">
<head>
<meta charset="utf-8">
<title>VoltMate Electrical Services – Spring Offer Flyer</title>
<link href="https://fonts.googleapis.com/css2?family=Oswald:wght@400;500;600;700&family=Marcellus+SC&family=Roboto+Condensed:wght@400&display=swap" rel="stylesheet">
<style>
  :root {
    --navy-deep: #1f2a63;
    --navy: #2c3a7e;
    --blue-mid: #5a67a8;
    --blue-light: #a3acd9;
    --orange: #f15a22;
    --white: #ffffff;
    --silver: #e6e8ef;
    --ink-blue: #1f2f6b;
  }
  * { margin: 0; padding: 0; box-sizing: border-box; }
  html, body { width: 856px; height: 1200px; overflow: hidden; background: var(--white); }
  .flyer {
    position: relative; width: 856px; height: 1200px; overflow: hidden;
    background: radial-gradient(ellipse 520px 560px at 50% 36%, var(--blue-light) 0%, var(--blue-mid) 45%, var(--navy) 80%, var(--navy-deep) 100%);
    color: var(--white);
    font-family: "Oswald", sans-serif;
    white-space: nowrap;
  }
  .brand { position: absolute; top: 82px; left: 0; width: 100%; text-align: center; }
  .brand-name { font-weight: 700; font-size: 100px; line-height: 1; letter-spacing: 2px; }
  .brand-sub { margin-top: 6px; font-weight: 600; font-size: 34px; line-height: 1.1; letter-spacing: 2px; }

  .offer-period {
    position: absolute; top: 302px; width: 100%; text-align: center;
    font-family: "Marcellus SC", serif; font-size: 30px; line-height: 40px; letter-spacing: 1px;
  }
  .offer-discount {
    position: absolute; top: 352px; width: 100%; height: 40px;
    display: flex; justify-content: center; align-items: center; gap: 16px;
    font-family: "Marcellus SC", serif; font-size: 26px; letter-spacing: 1px;
  }
  .offer-discount .pct { font-size: 34px; }
  .chevrons { width: 70px; height: 30px; }

  .band {
    position: absolute; left: 0; top: 664px; width: 100%; height: 265px;
    background: linear-gradient(180deg, rgba(255,255,255,0.08), rgba(255,255,255,0.03));
  }
  .service { position: absolute; top: 430px; width: 233px; }
  .service-card {
    height: 250px; border-top: 13px solid var(--orange);
    background: linear-gradient(180deg, rgba(255,255,255,0.28), rgba(255,255,255,0.1));
    display: flex; flex-direction: column; align-items: center; justify-content: center;
    text-transform: uppercase; line-height: 1; text-align: center;
    text-shadow: 0 2px 4px rgba(20,30,80,0.5);
    overflow: hidden;
  }
  .service-photo { margin-top: 20px; height: 174px; border: 1px solid rgba(255,255,255,0.8); }
  .photo-fan { background: linear-gradient(160deg, #d9dcd2, #b9bcb0 60%, #8f9288); }
  .photo-alarm { background: linear-gradient(160deg, #d8d5cd, #b4b0a7 70%, #99968e); }
  .photo-led { background: radial-gradient(ellipse at 50% 50%, #9b9ea3, #3c3d40 75%, #1b1b1d); }
  .service-caption {
    height: 56px; display: flex; align-items: center; justify-content: center;
    font-weight: 500; font-size: 30px; letter-spacing: 0.5px;
    background: linear-gradient(180deg, rgba(255,255,255,0.12), rgba(255,255,255,0));
  }
  .s1 { left: 37px; } .s2 { left: 311px; } .s3 { left: 585px; }

  .t-ceiling { font-weight: 600; font-size: 62px; }
  .t-fan { font-weight: 600; font-size: 98px; letter-spacing: -1px; margin-top: 2px; }
  .t-install { font-weight: 500; font-size: 34px; margin-top: 4px; }
  .t-smoke { font-weight: 600; font-size: 70px; }
  .t-small { font-weight: 500; font-size: 26px; letter-spacing: 0.5px; line-height: 1.4; }
  .t-led { font-weight: 600; font-size: 58px; margin-top: 2px; }
  .t-dl { font-weight: 600; font-size: 40px; margin-top: 2px; }

  .tagline-strip {
    position: absolute; top: 929px; left: 0; width: 100%; height: 82px;
    background: linear-gradient(180deg, #3a4788, #2e3b7c);
    display: flex; align-items: center; justify-content: center;
    font-weight: 600; font-size: 24px; letter-spacing: 1px;
  }
  .tagline-strip .name { margin-left: 8px; }

  .footer {
    position: absolute; top: 1011px; left: 0; width: 100%; height: 189px;
    border-top: 2px solid rgba(255,255,255,0.7);
    background: linear-gradient(180deg, #2c3a7e, #233069);
  }
  .contact-list { position: absolute; left: 30px; top: 18px; list-style: none; font-family: "Roboto Condensed", sans-serif; font-size: 22px; }
  .contact-list li { display: flex; align-items: center; height: 40px; }
  .contact-list svg { width: 28px; height: 28px; margin-right: 18px; }
  .service-area { position: absolute; left: 30px; top: 146px; font-family: "Roboto Condensed", sans-serif; font-size: 22px; line-height: 30px; text-transform: uppercase; }
  .call-now {
    position: absolute; right: 0; top: 3px; width: 356px; height: 64px;
    background: linear-gradient(90deg, rgba(255,255,255,0) 0%, rgba(230,232,239,0.75) 30%, var(--silver) 100%);
    display: flex; align-items: center; justify-content: flex-end; padding-right: 20px;
    font-weight: 600; font-size: 34px; letter-spacing: -0.5px; color: var(--ink-blue);
  }
  .expiry { position: absolute; right: 26px; top: 112px; text-align: right; font-family: "Marcellus SC", serif; }
  .expiry .label { font-size: 23px; line-height: 30px; }
  .expiry .date { font-size: 25px; line-height: 32px; }
</style>
</head>
<body>
<main class="flyer">
  <header class="brand">
    <div class="brand-name">VoltMate</div>
    <div class="brand-sub">Electrical Services</div>
  </header>

  <p class="offer-period">During the months of October &amp; November</p>
  <p class="offer-discount">
    <svg class="chevrons" viewBox="0 0 74 32" aria-hidden="true"><g fill="var(--orange)"><path d="M0 0h12l16 16-16 16H0l16-16z"/><path d="M22 0h12l16 16-16 16H22l16-16z"/><path d="M44 0h12l16 16-16 16H44l16-16z"/></g></svg>
    <span>Receive a <span class="pct">10%</span> discount on all services</span>
    <svg class="chevrons" viewBox="0 0 74 32" aria-hidden="true"><g fill="var(--orange)"><path d="M74 0H62L46 16l16 16h12L58 16z"/><path d="M52 0H40L24 16l16 16h12L36 16z"/><path d="M30 0H18L2 16l16 16h12L14 16z"/></g></svg>
  </p>

  <div class="band"></div>

  <section class="service s1">
    <div class="service-card"><span class="t-ceiling">Ceiling</span><span class="t-fan">Fan</span><span class="t-install">Installation</span></div>
    <div class="service-photo photo-fan" role="img" aria-label="Photo of a dark ceiling fan against a pale ceiling"></div>
    <div class="service-caption">KEEP COOL</div>
  </section>
  <section class="service s2">
    <div class="service-card"><span class="t-smoke">Smoke</span><span class="t-smoke">Alarm</span><span class="t-install">Installation</span></div>
    <div class="service-photo photo-alarm" role="img" aria-label="Photo of a white smoke alarm mounted on a ceiling"></div>
    <div class="service-caption">STAY SAFE</div>
  </section>
  <section class="service s3">
    <div class="service-card"><span class="t-small">Replace existing</span><span class="t-small">downlights for</span><span class="t-led">New LED</span><span class="t-dl">Downlights</span></div>
    <div class="service-photo photo-led" role="img" aria-label="Photo of several round LED downlights glowing"></div>
    <div class="service-caption">SAVE POWER</div>
  </section>

  <div class="tagline-strip">with <span class="name">VoltMate</span></div>

  <footer class="footer">
    <ul class="contact-list">
      <li><svg viewBox="0 0 30 30" aria-hidden="true"><circle cx="15" cy="15" r="15" fill="#fff"/><path d="M10 7.5l3 4-1.8 2a10 10 0 0 0 5.3 5.3l2-1.8 4 3-2 3C14 22.5 7.5 16 7.5 9.5z" fill="var(--navy)"/></svg>0400 555 019</li>
      <li><svg viewBox="0 0 30 30" aria-hidden="true"><circle cx="15" cy="15" r="15" fill="#fff"/><g fill="none" stroke="var(--navy)" stroke-width="1.6"><circle cx="15" cy="15" r="9"/><ellipse cx="15" cy="15" rx="4" ry="9"/><path d="M6 15h18M7.5 10.5h15M7.5 19.5h15"/></g></svg>www.voltmate.com.au</li>
      <li><svg viewBox="0 0 30 30" aria-hidden="true"><circle cx="15" cy="15" r="15" fill="#fff"/><rect x="8" y="10" width="14" height="10" fill="var(--navy)"/><path d="M8 10l7 6 7-6" fill="none" stroke="#fff" stroke-width="1.4"/></svg>info@voltmate.com.au</li>
    </ul>
    <p class="service-area">Serving the Northern Beaches since 2013</p>
    <div class="call-now">CALL NOW!&nbsp;CALL NOW!</div>
    <div class="expiry">
      <div class="label">Offer expires</div>
      <div class="date">30th November 2016</div>
    </div>
  </footer>
</main>
</body>
</html>
```